Virtualization software: PowerPoint, business cards

We're a young, small, dynamic application virtualization company: www.velrinta.com
We need a PowerPoint template + business cards. PDF background will be a plus.
This is mostly for enterprise clients.
Clean, professional, and most of all - following our website's colors.

Reason: Busy weekend; we'll need some more time to provide feedback & choose.

Target Market(s)

Corporate clients & investors.

Industry/Entity Type

Business

Requirements
Must have
• Clean, professional, and following our website's look: www.velrinta.com

```html
<!DOCTYPE html>
<html lang="en">
<head>
<meta charset="utf-8">
<title>Velrinta – Business Cards and Slide Template</title>
<link rel="stylesheet" href="https://fonts.googleapis.com/css2?family=Arimo:wght@400;700&display=swap">
<style>
  :root {
    --page: #ffffff;
    --card: #121212;
    --green: #6cc04a;
    --bright-green: #3df03a;
    --ink: #000000;
    --white: #ffffff;
    --soft-white: #e6e6e6;
    --slide-bg: #f2f2f2;
    --grey: #808080;
  }
  * { margin: 0; padding: 0; box-sizing: border-box; }
  html, body { width: 900px; height: 1200px; overflow: hidden; background: var(--page); }
  body { position: relative; font-family: "Arimo", Arial, sans-serif; }

  .card {
    position: absolute; top: 107px; width: 423px; height: 269px;
    background: var(--card); border-radius: 12px; overflow: hidden;
    border-top: 12px solid var(--green); border-bottom: 14px solid var(--green);
  }
  .card--front { left: 11px; }
  .card--back { left: 462px; }

  .brand-mark {
    position: absolute; left: 6px; right: 0; top: 96px; text-align: center;
    color: var(--white); font-size: 44px; font-weight: 400; letter-spacing: 6px; line-height: 1;
  }
  .brand-url {
    position: absolute; left: 6px; right: 0; top: 146px; text-align: center;
    color: var(--soft-white); font-size: 9px; font-weight: 700; letter-spacing: 6px;
  }

  .person-name { position: absolute; left: 51px; top: 95px; color: var(--white); font-size: 24px; line-height: 1; }
  .person-role { position: absolute; left: 51px; top: 121px; color: var(--soft-white); font-size: 12px; font-weight: 700; }
  .divider {
    position: absolute; left: 212px; top: 60px; width: 3px; height: 126px;
    background: linear-gradient(to bottom, transparent, var(--green) 45%, #b8f0a0 55%, transparent);
  }
  .contact {
    position: absolute; left: 249px; top: 105px; color: var(--soft-white);
    font-size: 8.5px; font-weight: 700; line-height: 9px;
  }
  .contact p + p { margin-top: 8px; }

  .slide {
    position: absolute; left: 0; top: 464px; width: 900px; height: 676px;
    background: var(--slide-bg); overflow: hidden;
  }
  .slide-header { position: absolute; left: 0; top: 0; width: 900px; height: 130px; }
  .slide-title {
    position: absolute; right: 26px; top: 268px; font-size: 62px; font-weight: 700;
    color: var(--ink); line-height: 1;
  }
  .slide-subtitle {
    position: absolute; right: 28px; top: 361px; font-size: 41.5px; font-weight: 700;
    color: var(--grey); line-height: 1;
  }
  .slide-footer {
    position: absolute; left: 0; bottom: 0; width: 900px; height: 27px; background: var(--ink);
  }
  .footer-brand {
    position: absolute; left: 10px; top: 3px; color: var(--white);
    font-size: 21px; letter-spacing: 3px; line-height: 1;
  }
  .footer-url {
    position: absolute; right: 20px; top: 5px; color: var(--bright-green);
    font-size: 15px; font-weight: 700;
  }
</style>
</head>
<body>
  <section class="card card--front">
    <div class="brand-mark">VELRINTA</div>
    <div class="brand-url">www.velrinta.com</div>
  </section>

  <section class="card card--back">
    <div class="person-name">Daniel Hart</div>
    <div class="person-role">Job Title</div>
    <div class="divider"></div>
    <div class="contact">
      <p>48 Harbor Lane<br>Northfield, 204518</p>
      <p>danielhart@mailbox.com<br>www.velrinta.com</p>
    </div>
  </section>

  <section class="slide">
    <svg class="slide-header" viewBox="0 0 900 130" role="img" aria-label="Header band with green and white light streaks on black">
      <defs>
        <linearGradient id="header-tone" x1="0" y1="0" x2="1" y2="0.4">
          <stop offset="0" stop-color="#0c2a0a"/>
          <stop offset="0.35" stop-color="#000000"/>
          <stop offset="0.7" stop-color="#0f3a0c"/>
          <stop offset="1" stop-color="#000000"/>
        </linearGradient>
      </defs>
      <path d="M0 0 H900 V122 C840 70 760 48 640 48 C480 48 380 100 240 100 C140 100 60 95 0 85 Z" fill="url(#header-tone)"/>
    </svg>
    <h1 class="slide-title">Click to add title</h1>
    <h2 class="slide-subtitle">Click to add subtitle</h2>
    <footer class="slide-footer">
      <span class="footer-brand">VELRINTA</span>
      <span class="footer-url">www.velrinta.com</span>
    </footer>
  </section>
</body>
</html>
```